MEDICAL CLINIC LETTERHEAD

Design is a letterhead for a non-profit medical center. The name of the clinic is VYRLOTEN Community Health Center. Although the full name must be included, the community health center part is more of a description and should be less visible - i attached an example of what I mean by that (ATTACHED IMAGE IS AN EXAMPLE OF FONT SIZES NOT A DESIGN IDEA). Please design something modern, cool looking and unique because I can always download free templates.
Phone, email, website and etc will be added later.

Industry/Entity Type

MEDICAL

```html
<!DOCTYPE html>
<html lang="en">
<head>
<meta charset="utf-8">
<title>VYRLOTEN Community Health Center – Letterhead</title>
<link rel="stylesheet" href="https://fonts.googleapis.com/css2?family=Lato:wght@400;700&family=Poppins:wght@400;500&display=swap">
<style>
  :root {
    --navy: #2c3558;
    --green: #0d9466;
    --ink: #2b2b2b;
    --muted: #4a4a4a;
    --paper: #ffffff;
    --backdrop: #e2e3e4;
    --sig-fill: #f1f1f2;
  }
  * { margin: 0; padding: 0; box-sizing: border-box; }
  html, body { width: 1200px; height: 1200px; overflow: hidden; background: var(--backdrop); }
  .canvas { width: 1200px; height: 1200px; display: flex; align-items: center; justify-content: center; }
  .letterhead {
    position: relative; width: 806px; height: 1140px; background: var(--paper);
    box-shadow: 0 6px 24px rgba(0,0,0,.12); font-family: "Lato", sans-serif; color: var(--ink);
  }
  .brand { position: absolute; top: 84px; left: 0; right: 0; text-align: center; }
  .brand-name {
    font-family: "Lato", sans-serif; font-weight: 700; font-size: 58px; letter-spacing: 4px;
    color: var(--navy); line-height: 1;
  }
  .brand-descriptor {
    margin-top: 10px; font-family: "Lato", sans-serif; font-weight: 400; font-size: 13px;
    letter-spacing: 6px; text-transform: uppercase; color: var(--green);
  }
  .recipient {
    position: absolute; top: 290px; left: 90px; font-size: 14px; line-height: 19px; color: var(--muted);
  }
  .salutation { position: absolute; top: 408px; left: 120px; font-size: 14px; color: var(--muted); }
  .body-copy {
    position: absolute; top: 448px; left: 120px; width: 600px; font-size: 14px; line-height: 23px;
    color: var(--ink); text-align: justify;
  }
  .closing { position: absolute; top: 792px; left: 120px; font-size: 14px; color: var(--muted); }
  .signature {
    position: absolute; top: 824px; left: 140px; width: 260px; height: 96px;
    background: var(--sig-fill); border-radius: 4px;
  }
  .contact {
    position: absolute; right: 60px; bottom: 62px; text-align: right;
    font-family: "Poppins", sans-serif; color: var(--ink);
  }
  .contact-row { display: flex; justify-content: flex-end; align-items: center; gap: 16px; font-size: 12px; font-weight: 500; }
  .contact-item { display: inline-flex; align-items: center; gap: 5px; }
  .contact-item svg { width: 11px; height: 11px; fill: var(--green); }
  .web-accent { color: var(--green); }
  .addresses { margin-top: 6px; font-size: 11px; font-weight: 400; color: var(--muted); }
  .footer-band { position: absolute; left: 0; right: 0; bottom: 0; height: 22px; display: flex; }
  .band-navy-left { width: 22%; background: var(--navy); }
  .band-green { flex: 1; background: var(--green); }
  .band-navy-right { width: 12%; background: var(--navy); }
</style>
</head>
<body>
<div class="canvas">
  <main class="letterhead">
    <header class="brand">
      <div class="brand-name">VYRLOTEN</div>
      <div class="brand-descriptor">Community Health Center</div>
    </header>

    <address class="recipient" style="font-style:normal">
      Mr. Adrian Pell<br>
      President<br>
      Northfield Advisors<br>
      111 Street Name,<br>
      City State, 12345
    </address>

    <p class="salutation">Dear :</p>

    <p class="body-copy">
      Lorem ipsum dolor sit amet, consectetur adipiscing elit. Aenean ut ipsum eget massa hendrerit
      vestibulum vel in velit. Donec pretium neque velit.
      Aliquam porta lectus nec mauris ornare venenatis. Vivamus non est turpis, et cursus sem. Mauris
      vehicula erat in diam auctor at bibendum nisl lacinia.
      Morbi imperdiet neque vehicula nunc convallis gravida. Vestibulum iaculis pretium placerat. Integer
      consequat, est sit amet facilisis eleifend, nibh nibh varius orci, eget dapibus arcu dui non purus.
      Pellentesque in magna mauris. Duis enim sapien, dictum vitae condimentum a, pulvinar vel lacus.
      Mauris et molestie nibh. Vestibulum vitae nulla at metus elementum porta sit amet interdum elit.
      Nulla sollicitudin neque eu nulla volutpat congue.
      Etiam pellentesque, velit id dapibus fermentum, turpis sapien ornare dui, ac tincidunt ligula odio
      congue purus. Nunc sed ante dui, in porta lectus. Cras nec sem lorem. In hac habitasse platea dictumst.
      Maecenas id diam quis dui porta tristique. Sed id egestas felis. Donec ullamcorper mattis posuere.
      Phasellus fermentum eleifend tortor vel dapibus. Vestibulum ante ipsum.
    </p>

    <p class="closing">Sincerely,</p>
    <div class="signature" role="img" aria-label="Handwritten signature of the sender"></div>

    <footer class="contact">
      <div class="contact-row">
        <span class="contact-item">
          <svg viewBox="0 0 24 24" aria-hidden="true"><path d="M6.6 10.8a15.1 15.1 0 0 0 6.6 6.6l2.2-2.2a1 1 0 0 1 1-.25 11.4 11.4 0 0 0 3.6.57 1 1 0 0 1 1 1V20a1 1 0 0 1-1 1A17 17 0 0 1 3 4a1 1 0 0 1 1-1h3.5a1 1 0 0 1 1 1c0 1.25.2 2.45.57 3.57a1 1 0 0 1-.25 1z"/></svg>
          0134567281 - 0509182736
        </span>
        <span class="contact-item">
          <svg viewBox="0 0 24 24" aria-hidden="true"><path d="M2 5h20v14H2zm2 2v.5l8 5 8-5V7zm0 2.9V17h16V9.9l-8 5z"/></svg>
          info@vyrloten.com
        </span>
        <span class="contact-item">
          <svg viewBox="0 0 24 24" aria-hidden="true"><path d="M12 2a10 10 0 1 0 0 20 10 10 0 0 0 0-20zm6.9 9h-3a15 15 0 0 0-1.3-6A8 8 0 0 1 18.9 11zM12 4.1c.9 1.3 1.7 3.7 1.9 6.9h-3.8c.2-3.2 1-5.6 1.9-6.9zM9.4 5a15 15 0 0 0-1.3 6h-3A8 8 0 0 1 9.4 5zM5.1 13h3a15 15 0 0 0 1.3 6A8 8 0 0 1 5.1 13zm6.9 6.9c-.9-1.3-1.7-3.7-1.9-6.9h3.8c-.2 3.2-1 5.6-1.9 6.9zm2.6-.9a15 15 0 0 0 1.3-6h3a8 8 0 0 1-4.3 6z"/></svg>
          www.<span class="web-accent">vyrloten</span>.com
        </span>
      </div>
      <div class="addresses">0042 W. Alder Avenue, Suite 310, Larkfield, California 90211 &nbsp;|&nbsp; 017 Bramble St. Suite 4, Ostrow, CA 90308</div>
    </footer>

    <div class="footer-band" aria-hidden="true">
      <div class="band-navy-left"></div>
      <div class="band-green"></div>
      <div class="band-navy-right"></div>
    </div>
  </main>
</div>
</body>
</html>
```